Irrigation Business needs their business cards modernised and revamped

I would like to keep my current logo, colours and revamp the format of the card.

I would like the card to be clean yet important.

Im not sure if you include texture but i would like the named logo to be indented into the card etc.

show me something alive and free something thats clinical to the point yet has a feel of achievement. i would like people to go nice card.

Target Market(s)

high end clients, corporate, sports field manger, the guys that make the decisions

Industry/Entity Type

Business

Contact Information for Business Card

nformation to be included

Dorian Hesk (Director)
0487253916
dorian@tfcraft.biz
www.taddsfieldcrafts.com

instagram logo
google logo
facebook logo

Colors

Designer to choose colors to be used in the design.

Requirements
Nice to have
• indentations a really nice feel to the card good texture

```html
<!DOCTYPE html>
<html lang="en">
<head>
<meta charset="utf-8">
<title>Tadd's Field Crafts – Business Cards</title>
<link rel="stylesheet" href="https://fonts.googleapis.com/css2?family=Roboto:wght@400;500;700&display=swap">
<style>
  :root {
    --backdrop: #1d4f9c;
    --card: #ffffff;
    --brand-blue: #2f5fa8;
    --band-blue: #2d5c9e;
    --sky-blue: #3fa3da;
    --accent-line: #5bb4e4;
    --text-blue: #3a6fb5;
    --white: #ffffff;
  }
  * { box-sizing: border-box; margin: 0; padding: 0; }
  html, body { width: 1200px; height: 1200px; overflow: hidden; }
  body {
    background: var(--backdrop);
    font-family: "Roboto", Arial, sans-serif;
    position: relative;
  }
  .card {
    position: absolute;
    top: 465px;
    width: 369px;
    height: 222px;
    background: var(--card);
    overflow: hidden;
    box-shadow: 0 6px 14px rgba(0,0,0,0.35);
  }
  .card--front { left: 219px; }
  .card--back { left: 611px; }

  .brand-disc {
    position: absolute;
    border-radius: 50%;
    background: var(--sky-blue);
    border: 3px solid var(--brand-blue);
  }
  .brand-name {
    position: absolute;
    color: var(--brand-blue);
    font-weight: 700;
    text-align: center;
    letter-spacing: 0.02em;
    line-height: 1.1;
    white-space: nowrap;
  }

  .card--front .brand-disc { left: 69px; top: 15px; width: 60px; height: 60px; }
  .card--front .brand-name { left: 0; width: 198px; top: 80px; font-size: 17px; }

  .decor-disc {
    position: absolute;
    width: 156px; height: 156px;
    border-radius: 50%;
    background: var(--sky-blue);
    border: 4px solid var(--brand-blue);
    top: -11px;
  }
  .card--front .decor-disc { left: 303px; }
  .card--back .decor-disc { left: -88px; }

  .contact {
    position: absolute;
    left: 16px; top: 129px;
    font-size: 11px;
    line-height: 14px;
    color: var(--text-blue);
  }
  .contact__name { font-weight: 700; color: var(--brand-blue); }
  .contact__role { color: var(--sky-blue); font-weight: 500; }

  .social {
    position: absolute;
    top: 161px; left: 281px;
    display: flex; gap: 6px;
  }
  .social__square {
    width: 19px; height: 19px;
    border-radius: 4px;
    background: var(--band-blue);
  }

  .card--back .brand-disc { left: 145px; top: 36px; width: 78px; height: 78px; }
  .card--back .brand-name { left: 0; width: 369px; top: 124px; font-size: 23px; }

  .band { position: absolute; left: 0; bottom: 0; width: 369px; height: 40px; }
  .band__url {
    position: absolute;
    left: 0; bottom: 5px; width: 100%;
    text-align: center;
    color: var(--white);
    font-size: 9px;
    letter-spacing: 0.22em;
  }
</style>
</head>
<body>

  <section class="card card--front">
    <div class="brand-disc"></div>
    <div class="brand-name">TADD'S FIELD<br>CRAFTS</div>
    <div class="decor-disc"></div>
    <div class="contact">
      <p><span class="contact__name">Dorian Hesk</span> <span class="contact__role">(Director)</span></p>
      <p>0487253916</p>
      <p>dorian@tfcraft.biz</p>
    </div>
    <div class="social" aria-label="Social links">
      <span class="social__square"></span>
      <span class="social__square"></span>
      <span class="social__square"></span>
    </div>
    <svg class="band" viewBox="0 0 369 40" aria-hidden="true">
      <path d="M0 2 Q185 12 369 0" fill="none" stroke="var(--accent-line)" stroke-width="2"/>
      <path d="M0 8 Q185 16 369 4 L369 40 L0 40 Z" fill="var(--band-blue)"/>
    </svg>
    <p class="band__url">www.taddsfieldcrafts.com</p>
  </section>

  <section class="card card--back">
    <div class="decor-disc"></div>
    <div class="brand-disc"></div>
    <div class="brand-name">TADD'S FIELD CRAFTS</div>
    <svg class="band" viewBox="0 0 369 40" aria-hidden="true">
      <path d="M0 2 Q185 12 369 0" fill="none" stroke="var(--accent-line)" stroke-width="2"/>
      <path d="M0 8 Q185 16 369 4 L369 40 L0 40 Z" fill="var(--band-blue)"/>
    </svg>
    <p class="band__url">www.taddsfieldcrafts.com</p>
  </section>

</body>
</html>
```